Kestrel Valley Alpine Riders Society needs a business card design

We need a business card design for our newly incorporated KVARS. We are helping the NZ Chinese community, as well as everyone else, to organise ski & snowboarding trips, training, and equipments. The design should be creative, energetic, young and vibrant.

Industry/Entity Type

Social Club

Contact Information for Business Card

Logo; Kestrel Valley Alpine Riders Society; Name: Oliver Brandt; Position: President; Address: 42 Marwick Rd, Epsom, Auckland 1051; Mobile: 020 7826 1957; Email: oliver@kvars-club.example; Web: www.kvars-club.example

Requirements
Must have
• 1, The text "Kestrel Valley Alpine Riders Society" should be put together with the supplied logo file to form a new complete logo combination.
• 2, Final design files should be in Adobe Illustrator format and all text must be editable.
Nice to have
• two or three colours

```html
<!DOCTYPE html>
<html lang="en">
<head>
<meta charset="utf-8">
<title>Kestrel Valley Alpine Riders Society — Business Card</title>
<link href="https://fonts.googleapis.com/css2?family=Roboto:wght@400;500&family=Roboto+Condensed:wght@700&display=swap" rel="stylesheet">
<style>
  :root {
    --backdrop: #e3e3e3;
    --card-white: #f7f7f7;
    --navy: #02206f;
    --brand-blue: #1b86d4;
    --sky: #1fb3e8;
    --ink: #555555;
    --rule: #b9b9b9;
    --white: #ffffff;
  }
  * { margin: 0; padding: 0; box-sizing: border-box; }
  html, body {
    width: 1200px; height: 960px; overflow: hidden;
    background: var(--backdrop);
    font-family: "Roboto", Arial, sans-serif;
  }
  .card {
    position: absolute;
    width: 601px; height: 342px;
  }
  .card--front { left: 314px; top: 113px; background: var(--card-white); }
  .card--back  { left: 311px; top: 472px; background: var(--navy); }

  .lockup {
    position: absolute; left: 0; right: 0;
    display: flex; flex-direction: column; align-items: center;
  }
  .card--front .lockup { top: 62px; }
  .card--back .lockup { top: 106px; }

  .brand {
    display: flex; align-items: center; justify-content: center; gap: 12px;
    font-family: "Roboto Condensed", "Arial Narrow", sans-serif;
    font-weight: 700; font-size: 76px; line-height: 1; letter-spacing: 1px;
  }
  .brand__dot { width: 20px; height: 20px; border-radius: 50%; }
  .brand__full {
    margin-top: 8px;
    font-family: "Roboto Condensed", "Arial Narrow", sans-serif;
    font-weight: 700; font-size: 12.5px; line-height: 1;
    letter-spacing: 2px; text-transform: uppercase;
  }
  .card--front .brand { color: var(--brand-blue); }
  .card--front .brand__dot { background: var(--brand-blue); }
  .card--front .brand__full { color: var(--navy); }
  .card--back .brand { color: var(--white); }
  .card--back .brand__dot { background: var(--white); }
  .card--back .brand__full { color: var(--white); }

  .holder {
    position: absolute; right: 342px; top: 226px; text-align: right;
  }
  .holder__name {
    font-family: "Roboto Condensed", "Arial Narrow", sans-serif;
    font-weight: 700; font-size: 21px; color: var(--navy); text-transform: uppercase;
  }
  .holder__role {
    font-family: "Roboto Condensed", "Arial Narrow", sans-serif;
    font-weight: 700; font-size: 16px; color: var(--sky); text-transform: uppercase; margin-top: 2px;
  }
  .divider {
    position: absolute; left: 279px; top: 195px; width: 1px; height: 104px; background: var(--rule);
  }
  .contact {
    position: absolute; left: 300px; top: 194px;
    font-size: 14.5px; color: var(--ink); line-height: 19px;
  }
  .contact__address { margin-bottom: 9px; }
  .contact__line { display: flex; align-items: center; gap: 6px; }
  .contact__line svg { width: 13px; height: 13px; fill: var(--navy); flex: none; }

  .back-url {
    position: absolute; left: 0; right: 0; top: 292px; text-align: center;
    color: var(--white); font-size: 13px; letter-spacing: 5.5px;
  }
</style>
</head>
<body>
  <section class="card card--front" aria-label="Card front">
    <div class="lockup">
      <div class="brand"><span class="brand__dot"></span>KVARS</div>
      <div class="brand__full">Kestrel Valley Alpine Riders Society</div>
    </div>
    <div class="holder">
      <div class="holder__name">Oliver Brandt</div>
      <div class="holder__role">President</div>
    </div>
    <div class="divider"></div>
    <div class="contact">
      <div class="contact__address">42 Marwick Rd, Epsom<br>Auckland 1051</div>
      <div class="contact__line">
        <svg viewBox="0 0 13 13" aria-hidden="true"><path d="M3.5 0h6a1 1 0 0 1 1 1v11a1 1 0 0 1-1 1h-6a1 1 0 0 1-1-1V1a1 1 0 0 1 1-1zm.5 1.5v8.5h5V1.5zM6.5 10.8a.7.7 0 1 0 0 1.4.7.7 0 0 0 0-1.4z"/></svg>
        <span>020 7826 1957</span>
      </div>
      <div class="contact__line">
        <svg viewBox="0 0 13 13" aria-hidden="true"><path d="M0 3h13v7.5H0zm1 .8v.3l5.5 3.4L12 4.1v-.3zm0 1.4v4.5h11V5.2L6.5 8.6z"/></svg>
        <span>oliver@kvars-club.example</span>
      </div>
      <div class="contact__line">
        <svg viewBox="0 0 13 13" aria-hidden="true"><circle cx="6.5" cy="6.5" r="6"/><path d="M3 4c1 .3 1.5 1 1.2 2S5 8 5.5 9.5 4 11 3.5 10 2 6 3 4zM7.5 1.8c1 .5 2 .2 2.8 1.4-.6.7-1.6.3-2 1.2s.8 1.5.3 2.3-1.6-.4-2-1.3.3-2.7.9-3.6z" fill="#f7f7f7"/></svg>
        <span>www.kvars-club.example</span>
      </div>
    </div>
  </section>

  <section class="card card--back" aria-label="Card back">
    <div class="lockup">
      <div class="brand"><span class="brand__dot"></span>KVARS</div>
      <div class="brand__full">Kestrel Valley Alpine Riders Society</div>
    </div>
    <div class="back-url">www.kvars-club.example</div>
  </section>
</body>
</html>
```